Educational Software Company Seeking Event Postcard Design

We are looking for a postcard promoting an upcoming event. We would like to utilize the red, white and blue color scheme that you will see on the site at: http://buildingcrafters.campuswren.example/ksx. Gray can also be used. Please feel free to add some extra design elements. This postcard is targeting education operations professionals.

7th Annual Northern New England Plantworks Summit Gathering

When: February 27th -28th

Where: Portsmouth, New Hampshire

Call to action - Register Today: linkhop.example/PSG-Register

I have attached a word containing the text I'd like you to use and an example template. Some design elements will need to be added to the template

Red = bf1e2d
Blue = 0054a6

Target Market(s)

education operations professionals

Industry/Entity Type

Education

Requirements
Must have
• Plantworks Summit Gathering logo, name of conference, date, location, blue, red, white and gray seen on website:

Red = bf1e2d
Blue = 0054a6

When: February 27th -28th

```html
<!DOCTYPE html>
<html lang="en">
<head>
<meta charset="utf-8">
<title>Plantworks Summit Gathering – Postcard</title>
<link rel="stylesheet" href="https://fonts.googleapis.com/css2?family=Cinzel:wght@500;700&family=Open+Sans:ital,wght@0,400;0,600;0,700;1,600&display=swap">
<style>
:root{
  --red:#bf1e2d;
  --blue:#0054a6;
  --gray:#939598;
  --line-gray:#a7a9ac;
  --white:#ffffff;
  --ink:#231f20;
  --pale-blue:#e6edf6;
}
*{box-sizing:border-box;margin:0;padding:0}
html,body{width:911px;height:1200px;overflow:hidden;background:var(--white)}
body{position:relative;font-family:"Open Sans",Arial,sans-serif;color:var(--ink)}

.card{position:absolute;left:26px;width:831px;height:534px;overflow:hidden;background:var(--white)}
.card--front{top:33px}
.card--back{top:601px;border:1px solid var(--line-gray);
  background:linear-gradient(90deg,var(--pale-blue) 0,var(--white) 70px)}

/* front */
.front__top-rule{position:absolute;left:0;top:0;width:100%;height:17px;background:var(--gray)}
.front__banner{position:absolute;left:0;top:17px;width:100%;height:155px;background:var(--blue)}
.front__fade{position:absolute;left:0;top:22px;width:344px;height:26px;
  background:linear-gradient(90deg,rgba(255,255,255,.95),rgba(255,255,255,0))}
.front__title{position:absolute;left:230px;width:555px;top:30px;text-align:center;color:var(--white);
  font-family:"Cinzel",Georgia,serif;font-weight:700;line-height:1}
.front__title .edition{display:block;font-size:40px;margin-bottom:12px}
.front__title .name{display:block;font-size:27px;line-height:41px}
.front__mid-rule{position:absolute;left:0;top:172px;width:100%;height:13px;background:var(--gray)}
.front__stripe{position:absolute;left:0;width:100%;height:6px;background:var(--blue)}
.front__stripe--top{top:207px}
.front__stripe--bottom{top:263px}
.front__date{position:absolute;left:264px;right:0;top:219px;height:38px;background:var(--red);color:var(--white);
  font-weight:700;font-size:19px;line-height:38px;padding-left:24px}
.front__seal{position:absolute;left:-6px;top:87px;width:280px;height:280px;border-radius:50%;background:var(--white);
  display:flex;align-items:center;justify-content:center;text-align:center}
.seal__name{font-family:"Cinzel",Georgia,serif;font-weight:700;color:var(--red);font-size:26px;line-height:1.2;width:190px}
.front__hosted{position:absolute;left:300px;top:365px;width:156px;text-align:right;color:var(--blue);
  font-style:italic;font-weight:600;font-size:15px;line-height:21px}
.host-badge{position:absolute}
.host-badge--one{left:478px;top:325px;width:74px;height:112px;background:#a9c2e6;border-radius:6px}
.host-badge--two{left:570px;top:330px;width:110px;height:104px;border:2px solid #2e8b3e;border-radius:6px}
.host-badge--three{left:688px;top:322px;width:72px;height:116px;background:#f2c230;border-radius:36px}
.front__bottom-rule{position:absolute;left:0;top:454px;width:100%;height:12px;background:var(--gray)}
.front__register{position:absolute;left:0;top:466px;width:100%;height:68px;background:var(--blue);color:var(--white);
  text-align:center;font-weight:700;font-size:21px;line-height:68px}

/* back */
.back__brand{position:absolute;left:36px;top:46px;display:flex;align-items:center;gap:14px}
.brand__mark{width:76px;height:76px;border-radius:50%;background:var(--blue)}
.brand__name{font-family:"Cinzel",Georgia,serif;font-weight:500;color:var(--blue);font-size:20px;line-height:30px;letter-spacing:.5px}
.back__date{position:absolute;left:36px;top:168px;width:424px;height:32px;border-radius:16px;background:var(--blue);color:var(--white);
  font-weight:600;font-size:15.5px;line-height:32px;padding-left:14px}
.back__intro{position:absolute;left:48px;top:212px;width:413px;font-size:13.6px;line-height:20.5px;text-align:justify}
.back__topics{position:absolute;left:172px;top:321px;list-style:none;font-size:14px;line-height:24.3px}
.back__topics li::before{content:"";display:inline-block;width:5px;height:5px;border-radius:50%;background:var(--blue);
  margin-right:11px;vertical-align:middle;position:relative;top:-2px}
.back__register{position:absolute;left:36px;top:456px;width:425px;height:33px;border-radius:16px;background:var(--red);color:var(--white);
  text-align:center;font-weight:600;font-size:16.5px;line-height:33px;letter-spacing:.3px}
.back__divider{position:absolute;left:551px;top:38px;width:2px;height:450px;background:var(--gray)}
.back__sender{position:absolute;left:565px;top:78px;width:130px;text-align:center}
.sender__name{font-weight:700;color:#0a8fc4;font-size:22px;line-height:1.1;margin-bottom:10px}
.sender__address{font-style:normal;font-size:11px;line-height:14px;color:var(--ink)}
</style>
</head>
<body>

<section class="card card--front" aria-label="Postcard front">
  <div class="front__top-rule"></div>
  <div class="front__banner"></div>
  <div class="front__fade"></div>
  <h1 class="front__title">
    <span class="edition">7th Annual</span>
    <span class="name">Northern New England Plantworks</span>
    <span class="name">Summit Gathering</span>
  </h1>
  <div class="front__mid-rule"></div>
  <div class="front__stripe front__stripe--top"></div>
  <p class="front__date">February 27th - 28th in Portsmouth, New Hampshire</p>
  <div class="front__stripe front__stripe--bottom"></div>
  <div class="front__seal"><span class="seal__name">Plantworks Summit Gathering</span></div>
  <p class="front__hosted">This conference is proudly hosted by:</p>
  <div class="host-badge host-badge--one" role="img" aria-label="Host partner badge: Granite Circle of School Finance Staff"></div>
  <div class="host-badge host-badge--two" role="img" aria-label="Host partner badge: Pine Coast Guild of School Finance Officers"></div>
  <div class="host-badge host-badge--three" role="img" aria-label="Host partner badge: CampusWren"></div>
  <div class="front__bottom-rule"></div>
  <p class="front__register">Register Today: linkhop.example/PSG-Register</p>
</section>

<section class="card card--back" aria-label="Postcard back">
  <div class="back__brand">
    <span class="brand__mark"></span>
    <span class="brand__name">Northern New England<br>Plantworks Summit Gathering</span>
  </div>
  <p class="back__date">February 27th - 28th in Portsmouth, New Hampshire</p>
  <p class="back__intro">This 2 - day conference is packed with specialized networking, leadership and learning opportunities focused on facility and maintenance fundamentals for solving everyday challenges and achieving operational excellence. Some that will be discussed include:</p>
  <ul class="back__topics">
    <li>Facilities Management</li>
    <li>Energy Management</li>
    <li>Personnel Management</li>
    <li>School Safety</li>
    <li>Sustainability</li>
  </ul>
  <p class="back__register">Register Today: linkhop.example/PSG-Register</p>
  <div class="back__divider"></div>
  <div class="back__sender">
    <p class="sender__name">CampusWren</p>
    <address class="sender__address">4200 Meridian Loop<br>Suite #210<br>Alder NC, 27000</address>
  </div>
</section>

</body>
</html>
```